Latin script tatoo design

Design of an old Latin script by Tervio - "Imperare Sibi Maximum Imperium Est". Translates as “To rule yourself is the ultimate power.".

• Script should use an old Latin font. It is desirable that the design includes some small detail or two, which symbolize willpower, perseverance etc. The script should be in two lines. The tattoo will be done on the arm.

```html
<!DOCTYPE html>
<html lang="la">
<head>
<meta charset="utf-8">
<title>Imperare Sibi Maximum Imperium Est</title>
<link rel="stylesheet" href="https://fonts.googleapis.com/css2?family=Almendra+SC&display=swap">
<style>
  :root {
    --ink: #1f0a0c;
    --frame: #2a2022;
    --paper: #ffffff;
    --canvas: #ffffff;
  }
  html, body {
    margin: 0;
    padding: 0;
    width: 1200px;
    height: 305px;
    overflow: hidden;
    background: var(--canvas);
  }
  .tattoo-banner {
    position: absolute;
    left: 78px;
    top: 44px;
    width: 1038px;
    height: 209px;
    background: var(--frame);
  }
  .tattoo-banner__field {
    position: absolute;
    inset: 12px 14px;
    background: var(--paper);
    border-radius: 10px;
    box-shadow: inset 0 0 14px 6px rgba(42, 32, 34, 0.55);
  }
  .tattoo-banner__art {
    position: absolute;
    inset: 0;
  }
  .motto {
    font-family: "Almendra SC", serif;
    fill: var(--ink);
  }
  .motto__line--top { font-size: 92px; }
  .motto__line--bottom { font-size: 60px; }
  .emblem-area { fill: var(--ink); }
</style>
</head>
<body>
  <div class="tattoo-banner">
    <div class="tattoo-banner__field"></div>
    <svg class="tattoo-banner__art" width="1038" height="209" viewBox="0 0 1038 209">
      <text class="motto motto__line--top" x="58" y="108" textLength="737" lengthAdjust="spacingAndGlyphs">IMPERARE SIBI</text>
      <text class="motto motto__line--bottom" x="58" y="176" textLength="709" lengthAdjust="spacingAndGlyphs">MAXIMVM IMPERIVM EST</text>
      <ellipse class="emblem-area" cx="886" cy="104" rx="80" ry="72" role="img" aria-label="Ornamental symbol of willpower and perseverance"/>
    </svg>
  </div>
</body>
</html>
```